National hospice pharmacy network needs a powerpoint design

We need a power point design for a new company that is creating a network of independent pharmacies to provide medication delivery to hospice patients in their area. We will be providing them with logistics to build a delivery system, software to increase efficiency and the marketing to hospice agencies. The pharmacies will benefit with increasing their patient care, increasing their efficiency and increasing their profits.

Pharmacy

```html
<!DOCTYPE html>
<html lang="en">
<head>
<meta charset="utf-8">
<title>CareReach – Presentation Slides</title>
<link rel="stylesheet" href="https://fonts.googleapis.com/css2?family=Fauna+One&family=Noto+Serif:ital@1&display=swap">
<style>
  :root {
    --backdrop: #6f7074;
    --slide: #ffffff;
    --brand-blue: #2556a0;
    --brand-green: #3bad4a;
    --ink: #1c1c1c;
    --ink-soft: #555555;
    --shadow: rgba(0, 0, 0, 0.55);
  }
  * { margin: 0; padding: 0; box-sizing: border-box; }
  html, body {
    width: 847px;
    height: 1200px;
    overflow: hidden;
    background: var(--backdrop);
    font-family: "Fauna One", Georgia, serif;
  }
  .canvas { position: relative; width: 847px; height: 1200px; }

  .slide {
    position: absolute;
    background: var(--slide);
    box-shadow: 8px 8px 6px var(--shadow);
  }
  .slide--title { left: 93px; top: 68px; width: 668px; height: 502px; }
  .slide--content { left: 93px; top: 626px; width: 669px; height: 502px; }

  .brand-name {
    position: absolute;
    color: var(--brand-blue);
    font-family: "Fauna One", Georgia, serif;
    letter-spacing: -1px;
    white-space: nowrap;
  }
  .slide--title .brand-name { left: 28px; top: 180px; font-size: 42px; }
  .rule-line { position: absolute; left: 0; top: 0; }

  .tagline {
    position: absolute;
    left: 346px;
    top: 331px;
    font-size: 15px;
    font-weight: bold;
    color: var(--ink);
  }
  .web-address {
    position: absolute;
    left: 0; right: 0;
    top: 466px;
    text-align: center;
    font-size: 13px;
    color: var(--ink-soft);
  }

  .slide-number {
    position: absolute;
    left: 33px; top: 0;
    width: 39px; height: 34px;
    background: var(--brand-green);
    color: #fff;
    font-family: Arial, sans-serif;
    font-size: 14px;
    line-height: 34px;
    text-align: center;
  }
  .slide-title {
    position: absolute;
    left: 0; right: 0;
    top: 53px;
    padding-left: 26px;
    text-align: center;
    font-family: "Noto Serif", Georgia, serif;
    font-style: italic;
    font-weight: normal;
    font-size: 24px;
    color: var(--ink);
  }
  .benefit-list {
    position: absolute;
    left: 66px;
    top: 128px;
    list-style: none;
  }
  .benefit {
    position: relative;
    padding-left: 26px;
    font-size: 12.5px;
    line-height: 18.7px;
    color: var(--ink);
  }
  .benefit::before {
    content: "➢";
    position: absolute;
    left: 0;
    font-size: 11px;
    font-family: "Segoe UI Symbol", sans-serif;
  }
  .benefit-details { list-style: none; }
  .benefit-detail {
    position: relative;
    padding-left: 29px;
    font-size: 11.6px;
    color: var(--ink-soft);
    white-space: nowrap;
  }
  .benefit-detail::before {
    content: "•";
    position: absolute;
    left: 15px;
    color: var(--ink);
  }

  .slide-footer .brand-name { left: 20px; top: 446px; font-size: 24px; letter-spacing: -0.8px; }
  .footer-band { position: absolute; top: 457px; height: 11px; }
  .footer-band--blue { left: 156px; width: 251px; background: var(--brand-blue); }
  .footer-band--green { left: 407px; width: 262px; background: var(--brand-green); }
</style>
</head>
<body>
<main class="canvas">

  <section class="slide slide--title" aria-label="Title slide">
    <span class="brand-name">CareReach</span>
    <svg class="rule-line" width="668" height="240" aria-hidden="true">
      <line x1="28" y1="229" x2="668" y2="223" stroke="#3bad4a" stroke-width="3"/>
    </svg>
    <p class="tagline">Helping your pharmacy expand</p>
    <p class="web-address">www.carereachnetwork.com</p>
  </section>

  <section class="slide slide--content" aria-label="Increased Efficiencies slide">
    <div class="slide-number">1</div>
    <h2 class="slide-title">Increased Efficiencies</h2>
    <ul class="benefit-list">
      <li class="benefit">No data entry
        <ul class="benefit-details">
          <li class="benefit-detail">Software that seamlessly communicates between prescribers and your pharmacy</li>
          <li class="benefit-detail">Essentially the hospice&nbsp; does all the data entry</li>
        </ul>
      </li>
      <li class="benefit">No phone calls
        <ul class="benefit-details">
          <li class="benefit-detail">All scripts new and refill done electronically</li>
          <li class="benefit-detail">Clinical consultation done by contracted&nbsp; pharmacists</li>
        </ul>
      </li>
      <li class="benefit">No third party billing
        <ul class="benefit-details">
          <li class="benefit-detail">Billing and Medicare reporting done for you</li>
        </ul>
      </li>
    </ul>
    <div class="slide-footer">
      <span class="brand-name">CareReach</span>
      <div class="footer-band footer-band--blue"></div>
      <div class="footer-band footer-band--green"></div>
    </div>
  </section>

</main>
</body>
</html>
```